Site Update/Merger: TWR Dynamics

We want to take some content (not ALL the content, but only what is specified) from two or our sites and combine into one
The New Website is in Wordpress too.
The new site needs to be a nice merge between these sites:
◦ https://brontavo-works.example/
◦ https://taskmira-launch.example/
Theme/topic: this is an Engineering site
The blog must be included on the home page (maybe smaller), and also on the Systems Engineering page (maybe a little bigger, allow the user to browse through all blogs)
Instructions and visual aids:
Step 1: SEE BRIEFING IN THE PDF ATTACHED
Step 2: some pictures for your reference (referenced in the PDF)

```html
<!DOCTYPE html>
<html lang="en">
<head>
<meta charset="utf-8">
<title>TWR Dynamics – Engineering Consulting</title>
<link rel="stylesheet" href="https://fonts.googleapis.com/css2?family=Roboto:wght@400;500;700&display=swap">
<style>
:root{
  --orange:#f96a0c;
  --blue:#3d8fd1;
  --ink:#111;
  --text:#2a2a2a;
  --muted:#666;
  --soft:#f8f8f8;
  --footer:#0b0b0b;
}
*{box-sizing:border-box;margin:0;padding:0}
html,body{width:1200px;height:2568px;overflow:hidden}
body{font-family:'Roboto',sans-serif;color:var(--text);background:#fff;position:relative}
.abs{position:absolute}

/* header */
.site-header{position:absolute;top:0;left:0;width:1200px;height:75px;background:#fff}
.brand{position:absolute;left:102px;top:20px;display:flex;align-items:center;gap:10px;font-size:28px;font-weight:700;color:var(--orange);letter-spacing:.5px}
.brand-dot{width:16px;height:16px;background:var(--orange)}
.main-nav{position:absolute;top:31px;left:424px;display:flex;font-size:17px;font-weight:500;color:var(--ink)}
.main-nav span{display:block}
.main-nav .current{color:var(--blue)}
.email-box{position:absolute;left:860px;top:16px;display:flex;align-items:center;gap:8px}
.email-icon{width:43px;height:43px;border-radius:50%;background:var(--blue);display:flex;align-items:center;justify-content:center}
.email-box small{display:block;font-size:14px;color:#333}
.email-box strong{display:block;font-size:17px;font-weight:500;color:var(--ink)}

/* hero */
.hero{position:absolute;top:75px;left:0;width:1200px;height:439px;
  background:radial-gradient(ellipse at 75% 40%,#3f8fc9 0%,#1f5e93 40%,#0e3a60 75%,#0a2a48 100%)}
.hero h1{position:absolute;left:102px;top:105px;font-size:56px;font-weight:700;color:#fff;letter-spacing:.5px}
.hero p{position:absolute;left:102px;top:176px;width:400px;font-size:19px;line-height:27px;font-weight:500;color:#fff}
.btn{position:absolute;left:102px;top:275px;width:168px;height:47px;border-radius:24px;background:var(--orange);color:#fff;font-size:16px;font-weight:700;display:flex;align-items:center;justify-content:center}

/* what we do */
.what-media{position:absolute;left:99px;top:588px;width:483px;height:168px;background:linear-gradient(120deg,#2c3138,#4a525c 50%,#23282e)}
.section-title{font-size:28px;font-weight:500;color:var(--orange)}
.what-text{position:absolute;left:628px;top:582px;width:470px}
.what-text p{margin-top:12px;font-size:17px;line-height:31.5px;color:#333}

/* services */
.services{position:absolute;top:840px;left:0;width:1200px;height:545px;
  background:linear-gradient(90deg,#efefef 0%,#eeeeee 40%,#b9b6b2 55%,#6d6a66 72%,#3a3a3c 100%)}
.services-copy{position:absolute;left:100px;top:73px;width:430px}
.services-copy .lead{font-size:16px;line-height:26px;font-weight:500;color:var(--ink);margin-top:6px}
.sub-title{font-size:21px;font-weight:500;color:var(--orange);margin-top:14px}
.focus{font-size:16px;color:var(--ink);margin-top:6px}
.value{position:absolute;left:100px;display:flex;gap:9px;width:430px}
.value-icon{flex:none;width:56px;height:56px;border-radius:50%;background:var(--orange);display:flex;align-items:center;justify-content:center}
.value h3{font-size:18px;font-weight:500;color:var(--orange);margin-top:0}
.value p{font-size:13px;line-height:21px;color:var(--ink);margin-top:2px}

/* physics */
.physics-media{position:absolute;left:70px;top:1420px;width:520px;height:370px;border-radius:40%;background:radial-gradient(ellipse at center,#3f55b8 0%,#8f9bd0 35%,#e3e6ef 65%,#fff 80%)}
.physics-text{position:absolute;left:655px;top:1512px;width:470px}
.physics-text h2{font-size:31px;line-height:33px;font-weight:500;color:var(--ink)}
.physics-text p{margin-top:15px;font-size:16px;line-height:32px;color:#222;padding-left:2px}

/* blogs */
.blogs{position:absolute;top:1835px;left:0;width:1200px;height:460px;background:var(--soft)}
.blogs h2{position:absolute;top:75px;width:1200px;text-align:center;font-size:38px;font-weight:700;color:var(--ink)}
.blog-card{position:absolute;top:182px;width:321px;height:197px;background:#fff;padding:42px 10px 0}
.blog-date{position:absolute;left:13px;top:-24px;width:165px;height:37px;background:var(--orange);color:#fff;font-size:14px;display:flex;align-items:center;justify-content:center;gap:6px}
.blog-card h3{font-size:18px;line-height:22px;font-weight:500;color:var(--ink)}
.blog-card p{margin-top:6px;font-size:13px;line-height:21px;color:var(--muted)}
.read-more{display:block;margin-top:6px;font-size:13px;font-weight:700;color:var(--orange)}

/* footer */
.site-footer{position:absolute;top:2295px;left:0;width:1200px;height:273px;background:var(--footer);color:#fff}
.footer-brand{position:absolute;top:82px;width:1200px;display:flex;justify-content:center;align-items:center;gap:10px;font-size:34px;font-weight:700;color:var(--orange)}
.footer-contact{position:absolute;top:168px;width:1200px;display:flex;justify-content:center;gap:22px;font-size:15px}
.footer-contact span{display:flex;align-items:center;gap:6px}
.copyright{position:absolute;top:211px;width:1200px;text-align:center;font-size:15px}
</style>
</head>
<body>

<header class="site-header">
  <div class="brand"><span class="brand-dot"></span>TWR Dynamics</div>
  <nav class="main-nav">
    <span class="current">HOME</span>
    <span style="margin-left:44px">|</span>
    <span style="margin-left:41px">SERVICES</span>
    <span style="margin-left:44px">|</span>
    <span style="margin-left:40px">CONTACT US</span>
  </nav>
  <div class="email-box">
    <div class="email-icon">
      <svg width="22" height="16" viewBox="0 0 22 16"><rect x="1" y="1" width="20" height="14" fill="none" stroke="#fff" stroke-width="1.6"/><path d="M1 1l10 8 10-8" fill="none" stroke="#fff" stroke-width="1.6"/></svg>
    </div>
    <div><small>Email Us</small><strong>info@taskmira-launch.example</strong></div>
  </div>
</header>

<section class="hero" role="img" aria-label="Close-up photo of a blue-lit electronic circuit board">
  <h1>WHO WE ARE</h1>
  <p>A Multi-Disciplinary Consulting &amp; Engineering Service Provider for theEV Industry and e-Mobility</p>
  <div class="btn">GET STARTED</div>
</section>

<div class="what-media" role="img" aria-label="Dark circuit board texture panel"></div>
<div class="what-text">
  <h2 class="section-title">WHAT WE DO</h2>
  <p>&nbsp;A team of automotive, control and mechanical engineers from different industries and backgrounds and with&nbsp; more than 10 years of experience that came together to provide cost effective and specialized services to your&nbsp; organization or team in the pursue of your projects goals.</p>
</div>

<section class="services" role="img" aria-label="Photo of an engineer with a laptop beside a network server rack">
  <div class="services-copy">
    <h2 class="section-title" style="font-size:24px">OUR SERVICES</h2>
    <p class="lead">This is just a glance at the activities and projects we can contribute to.For more details, go to our services menu or contact us to have a</p>
    <h3 class="sub-title">SYSTEMS ENGINEERING</h3>
    <p class="focus">Our Focus: Collaboration, Accountability and Feedback</p>
  </div>
  <div class="value" style="top:273px">
    <div class="value-icon"><svg width="30" height="30" viewBox="0 0 30 30" fill="#fff"><circle cx="15" cy="9" r="4"/><circle cx="7" cy="12" r="3"/><circle cx="23" cy="12" r="3"/><path d="M8 24c0-5 3-8 7-8s7 3 7 8z"/><path d="M2 23c0-4 2-6 5-6 1 0 2 .3 2.5.8C8 19.5 7.5 21 7.5 23z"/><path d="M28 23c0-4-2-6-5-6-1 0-2 .3-2.5.8 1.5 1.7 2 3.2 2 5.2z"/></svg></div>
    <div><h3>COLLABORATION</h3><p>Working together is the only way to&nbsp; maximize the team’s potential</p></div>
  </div>
  <div class="value" style="top:346px">
    <div class="value-icon"><svg width="24" height="30" viewBox="0 0 24 30"><rect x="2" y="4" width="20" height="25" rx="2" fill="none" stroke="#fff" stroke-width="2"/><rect x="8" y="1" width="8" height="5" fill="#fff"/><path d="M6 12l2 2 3-3M6 19l2 2 3-3" stroke="#fff" stroke-width="1.8" fill="none"/><path d="M13 13h5M13 20h5" stroke="#fff" stroke-width="2"/></svg></div>
    <div><h3>ACCOUNTABILITY</h3><p>Individual contributions are paramount to the team’s success</p></div>
  </div>
  <div class="value" style="top:419px">
    <div class="value-icon"><svg width="30" height="28" viewBox="0 0 30 28" fill="#fff"><path d="M5 2l1 2h2l-1.5 1.3.5 2L5 6 3 7.3l.5-2L2 4h2zM15 1l1 2h2l-1.5 1.3.5 2L15 5l-2 1.3.5-2L12 3h2zM25 2l1 2h2l-1.5 1.3.5 2L25 6l-2 1.3.5-2L22 4h2z"/><rect x="3" y="14" width="6" height="12"/><path d="M11 14l5-5c1-1 3 0 2.5 2L17 14h7c1.5 0 2.5 1.5 2 3l-2 7c-.4 1.2-1.3 2-2.5 2H11z"/></svg></div>
    <div><h3>FEEDBACK</h3><p>Clear Feedback methods are in place</p></div>
  </div>
</section>

<div class="physics-media" role="img" aria-label="Exploded view illustration of a car showing its components and wheels"></div>
<div class="physics-text">
  <h2>PHYSICS-BASED MODELING AND HARDWARE IN THE LOOP</h2>
  <p>From data-driven system identification to real-time mathematical models&nbsp; for your simulation; we can handle that work for you. In addition, we are&nbsp; highly skilled on HIL testing and can support you in design and build&nbsp; phases to satisfy complex validation testing.</p>
</div>

<section class="blogs">
  <h2>LATEST BLOGS</h2>
  <article class="blog-card" style="left:100px">
    <div class="blog-date"><svg width="12" height="12" viewBox="0 0 12 12" fill="#fff"><rect x="0" y="2" width="12" height="10" rx="1"/><rect x="2" y="0" width="2" height="3"/><rect x="8" y="0" width="2" height="3"/></svg>JUNE 04,2021</div>
    <h3>Design And Implementation<br>(The “how”)</h3>
    <p>by R. Havel, Taskmira Launch Team Follow the “what”, the “how”, and the “validation” as we navigate the ins and outs of the so-called</p>
    <span class="read-more">READ MORE ▸</span>
  </article>
  <article class="blog-card" style="left:440px">
    <div class="blog-date"><svg width="12" height="12" viewBox="0 0 12 12" fill="#fff"><rect x="0" y="2" width="12" height="10" rx="1"/><rect x="2" y="0" width="2" height="3"/><rect x="8" y="0" width="2" height="3"/></svg>JUNE 04,2021</div>
    <h3>What Is The Design Process And Why Is The System Broken?</h3>
    <p>by R. Havel, Taskmira Launch Team Follow the “what”, the “how”, and the “validation” as we navigate the ins and outs of the so-called</p>
    <span class="read-more">READ MORE ▸</span>
  </article>
  <article class="blog-card" style="left:781px">
    <div class="blog-date"><svg width="12" height="12" viewBox="0 0 12 12" fill="#fff"><rect x="0" y="2" width="12" height="10" rx="1"/><rect x="2" y="0" width="2" height="3"/><rect x="8" y="0" width="2" height="3"/></svg>JUNE 04,2021</div>
    <h3>How To Approach Requirement Definition In The Design Process</h3>
    <p>by R. Havel, Taskmira Launch Team Follow the “what”, the “how”, and the “validation” as we navigate the ins and outs of the so-called</p>
    <span class="read-more">READ MORE ▸</span>
  </article>
</section>

<footer class="site-footer">
  <div class="footer-brand"><span class="brand-dot" style="width:20px;height:20px"></span>TWR Dynamics</div>
  <div class="footer-contact">
    <span><svg width="10" height="14" viewBox="0 0 10 14"><path d="M5 0a5 5 0 015 5c0 4-5 9-5 9S0 9 0 5a5 5 0 015-5z" fill="#fff"/><circle cx="5" cy="5" r="2" fill="#0b0b0b"/></svg>North America Location: Alder Falls, SC</span>
    <span>|</span>
    <span><svg width="15" height="11" viewBox="0 0 15 11"><rect x=".7" y=".7" width="13.6" height="9.6" fill="none" stroke="#fff" stroke-width="1.3"/><path d="M.7.7l6.8 5.5L14.3.7" fill="none" stroke="#fff" stroke-width="1.3"/></svg>Email: info@taskmira-launch.example</span>
  </div>
  <div class="copyright">TWR DYNAMICS © 2021 ALL RIGHTS RESERVED</div>
</footer>

</body>
</html>
```